yourSmileCare Brookvale Business Card

Please design a two sided business card that is Elegant and Professional
Add subtle elegant patterns to suit Spot UV printing/ or raised printing

Name: Dr Marcus T. Fenwick
Qualification: BDSc (QLD)
Title: Dental Surgeon, Clinical Director
Company: yourSmileCare Brookvale
Phone: (02) 7593 2268
Address: Shop 7/18-20 Lindon Ave Brookvale 2097
email: info@yoursmilecarebrookvale.com.au
Facebook: facebook.com/yoursmilecarebrookvale

Motto:
Quality dentistry you can trust

Description of services (not compulsory):
Preventative Dentistry | General Dentistry
Cosmetic Dentistry | Teeth Whitening
Crown and Bridge | Root Canal Therapy
Veneers | Clearvono | Orthodontics
Emergency Dental Care | After Hours

Personalised Treatment Plans
Transparent Fees

Please make sure card is elegant and professional

Target Market(s)

general population, patients,
Dental sales companies, other professions

Industry/Entity Type

Dental Clinic

Contact Information for Business Card

Name: Dr Marcus T. Fenwick
Qualification: BDSc (QLD)
Phone: (02) 7593 2268
Address: Shop 7/18-20 Lindon Ave Brookvale

Motto:

Description of services (not compulsory)

Transparent Fees

Image of dental surgery optional

Please make sure card is elegant and profession

Requirements
Must have
• Logo
• Name, Title (next to name), Business
• Phone, address, facbeook
• Must have stylish design to suit SPOT UV reflective printing
Nice to have
• Subtle elegant patterns which will have Spot UV on them when printed
• Colours to match logo colour
• Description of services
Should not have
• Small fonts that are hard to read
• DO NOT PUT IMAGES OF DENTAL INSTRUMENTS OR TEETH PLEASE

```html
<!DOCTYPE html>
<html lang="en">
<head>
<meta charset="utf-8">
<title>yourSmileCare Brookvale – Business Card</title>
<link rel="stylesheet" href="https://fonts.googleapis.com/css2?family=Open+Sans:wght@400;600;700&display=swap">
<style>
  :root {
    --page-bg: #ecebe8;
    --card-white: #ffffff;
    --brand-green: #8cc63f;
    --green-tint: #9fd05a;
    --brand-grey: #77787b;
    --back-grey: #808285;
    --grey-tint: #8e9093;
    --text-light: #ffffff;
    --dot-green: #8cc63f;
  }
  * { margin: 0; padding: 0; box-sizing: border-box; }
  html, body {
    width: 1200px; height: 900px; overflow: hidden;
    background: var(--page-bg);
    font-family: "Open Sans", Arial, sans-serif;
  }
  .canvas { position: relative; width: 1200px; height: 900px; }

  .card {
    position: absolute; overflow: hidden;
    background: var(--card-white);
    box-shadow: 0 6px 18px rgba(0,0,0,0.18);
  }
  .card-front { left: 77px; top: 33px; width: 588px; height: 365px; }
  .card-back  { left: 388px; top: 505px; width: 567px; height: 352px; }

  .brand-name {
    position: absolute; color: var(--brand-grey); font-weight: 600;
    line-height: 1; white-space: nowrap;
  }
  .brand-name .brand-line { display: block; }
  .card-front .brand-name { left: 90px; top: 38px; font-size: 38px; }
  .card-front .brand-name .brand-line + .brand-line { font-size: 22px; margin-top: 6px; letter-spacing: 1px; }
  .brand-dot {
    position: absolute; left: 32px; top: 44px; width: 46px; height: 46px;
    border-radius: 50%; background: var(--brand-green);
  }
  .card-back .brand-name { left: 31px; top: 30px; font-size: 40px; }
  .card-back .brand-name .brand-line + .brand-line { font-size: 24px; margin-top: 6px; letter-spacing: 1px; }

  .band { position: absolute; left: 0; right: 0; bottom: 0; }
  .card-front .band { top: 134px; background: var(--brand-green); }
  .card-back .band { top: 125px; background: var(--back-grey); }

  .accent-circle { position: absolute; border-radius: 50%; }
  .card-front .accent-circle { left: 358px; top: 0; width: 62px; height: 62px; background: var(--green-tint); }
  .card-back .accent-circle { left: 372px; top: 0; width: 58px; height: 58px; background: var(--grey-tint); }

  .details { position: absolute; left: 31px; top: 12px; color: var(--text-light); }
  .doctor-name { font-size: 19px; font-weight: 700; line-height: 26px; }
  .doctor-name .qualification { font-size: 15px; font-weight: 600; margin-left: 6px; }
  .doctor-title { font-size: 15px; line-height: 24px; }
  .address { font-size: 15px; line-height: 22px; margin-top: 15px; margin-left: 1px; }
  .contact-list { list-style: none; margin-top: 8px; }
  .contact-list li { font-size: 15px; line-height: 25px; display: flex; align-items: center; }
  .contact-list svg { width: 12px; height: 12px; margin-right: 9px; fill: var(--text-light); flex: none; }
  .contact-list .no-icon { padding-left: 21px; }
  .motto { font-size: 15px; font-weight: 700; text-transform: uppercase; margin-top: 3px; line-height: 26px; }

  .services { position: absolute; left: 31px; top: 12px; color: var(--text-light); }
  .services-heading { font-size: 20px; font-weight: 600; line-height: 26px; margin-bottom: 6px; }
  .service-list { list-style: none; }
  .service-list li { font-size: 14px; font-weight: 600; line-height: 24px; white-space: nowrap; }
  .service-list .sep {
    display: inline-block; width: 6px; height: 6px; border-radius: 50%;
    background: var(--dot-green); margin: 0 9px 2px 11px; vertical-align: middle;
  }
</style>
</head>
<body>
<main class="canvas">

  <section class="card card-front" aria-label="Business card front">
    <span class="brand-dot"></span>
    <div class="brand-name"><span class="brand-line">yourSmileCare</span><span class="brand-line">Brookvale</span></div>
    <div class="band">
      <span class="accent-circle"></span>
      <div class="details">
        <p class="doctor-name">Dr Marcus T. Fenwick<span class="qualification">BDSc (QLD)</span></p>
        <p class="doctor-title">Dental Surgeon, Clinical Director</p>
        <p class="address">Shop 7/18-20 Lindon Ave Brookvale</p>
        <ul class="contact-list">
          <li><svg viewBox="0 0 24 24" aria-hidden="true"><path d="M6.6 10.8a15.2 15.2 0 0 0 6.6 6.6l2.2-2.2a1 1 0 0 1 1-.25 11.4 11.4 0 0 0 3.6.57 1 1 0 0 1 1 1V20a1 1 0 0 1-1 1A17 17 0 0 1 3 4a1 1 0 0 1 1-1h3.5a1 1 0 0 1 1 1c0 1.25.2 2.45.57 3.57a1 1 0 0 1-.25 1z"/></svg>(02) 7593 2268</li>
          <li><svg viewBox="0 0 24 24" aria-hidden="true"><path d="M2 5h20v14H2z M2 5l10 8 10-8" fill="none" stroke="#fff" stroke-width="0"/><path d="M2 6v13h20V6l-10 7.5z M3 5l9 6.8L21 5z"/></svg>info@yoursmilecarebrookvale.com.au</li>
          <li class="no-icon">yoursmilecarebrookvale</li>
        </ul>
        <p class="motto">Quality dentistry you can trust</p>
      </div>
    </div>
  </section>

  <section class="card card-back" aria-label="Business card back">
    <div class="brand-name"><span class="brand-line">yourSmileCare</span><span class="brand-line">BROOKVALE</span></div>
    <div class="band">
      <span class="accent-circle"></span>
      <div class="services">
        <h2 class="services-heading">Our Services</h2>
        <ul class="service-list">
          <li>Preventative Dentistry<span class="sep"></span>General Dentistry</li>
          <li>Cosmetic Dentistry<span class="sep"></span>Teeth Whitening</li>
          <li>Crown and Bridge<span class="sep"></span>Root Canal Therapy</li>
          <li>Veneers - Clearvono<span class="sep"></span>Orthodontics</li>
          <li>Emergency Dental Care<span class="sep"></span>After Hours</li>
          <li>Personalised Treatment Plans</li>
          <li>Transparent Fees</li>
        </ul>
      </div>
    </div>
  </section>

</main>
</body>
</html>
```